E-Waste Recycling Company Business Card

New Electronic Recycling Company based in Long Island, New York called "Lady Rust-a-bunch" We take outdated computers, components, electrical wire, circuit breakers, ink cartridges, etc. We look mostly for donated items that we recycle for our customers but will pay for large quantities from businesses. The design should reflect that we are environmentally friendly and our unique 7Q Obliteration process that ensures all personal data is wiped clean off hard drives. Please use our attached logo
Industry/Entity Type
Electrical

```html
<!DOCTYPE html>
<html lang="en">
<head>
<meta charset="utf-8">
<title>Lady Rust-a-bunch — Business Card</title>
<link rel="stylesheet" href="https://fonts.googleapis.com/css2?family=Cinzel:wght@400&family=Crimson+Pro:wght@400&display=swap">
<style>
  :root {
    --stage: #62bb47;
    --card: #0b0b0b;
    --green: #5cbf3f;
    --white: #ffffff;
    --cream: #e6e2d2;
    --shadow: rgba(0, 0, 0, 0.45);
  }
  * { margin: 0; padding: 0; box-sizing: border-box; }
  html, body {
    width: 1200px;
    height: 960px;
    overflow: hidden;
    background: var(--stage);
  }
  .canvas {
    position: relative;
    width: 1200px;
    height: 960px;
  }
  .card {
    position: absolute;
    left: 252px;
    width: 698px;
    height: 398px;
    background: var(--card);
    box-shadow: 3px 4px 6px var(--shadow);
    overflow: hidden;
  }
  .card--front { top: 63px; }
  .card--back { top: 497px; }

  .swoosh {
    position: absolute;
    left: 0;
    top: 0;
    width: 698px;
    height: 398px;
  }

  .brand-mark {
    position: absolute;
    border-radius: 50%;
    background: var(--green);
  }
  .card--front .brand-mark {
    left: 58px;
    top: 58px;
    width: 140px;
    height: 140px;
  }
  .card--back .brand-mark {
    left: 478px;
    top: 124px;
    width: 86px;
    height: 86px;
  }

  .brand-name {
    position: absolute;
    font-family: "Cinzel", serif;
    font-weight: 400;
    color: var(--white);
    text-transform: uppercase;
    white-space: nowrap;
  }
  .card--front .brand-name {
    left: 225px;
    top: 114px;
    font-size: 29px;
    letter-spacing: 2px;
  }
  .card--back .brand-name {
    left: 521px;
    top: 235px;
    transform: translateX(-50%);
    font-size: 16px;
    letter-spacing: 1px;
  }

  .contact {
    position: absolute;
    left: 82px;
    top: 76px;
    font-family: "Crimson Pro", serif;
    color: var(--green);
  }
  .contact__name {
    font-family: "Cinzel", serif;
    font-size: 27px;
    letter-spacing: 1px;
    line-height: 1;
  }
  .contact__title {
    margin-top: 23px;
    font-size: 13px;
    text-transform: uppercase;
  }
  .contact__address {
    margin-top: 16px;
    font-size: 13px;
  }
  .contact__list {
    list-style: none;
    font-size: 16px;
  }
  .contact__list--phones { margin-top: 32px; }
  .contact__list--online { margin-top: 18px; }
  .contact__list li {
    display: flex;
    align-items: center;
    height: 23px;
  }
  .contact__icon {
    width: 12px;
    height: 12px;
    margin-left: 8px;
    margin-right: 13px;
    fill: var(--green);
  }
</style>
</head>
<body>
<main class="canvas">

  <section class="card card--front" aria-label="Card front">
    <div class="brand-mark" aria-hidden="true"></div>
    <p class="brand-name">Lady Rust-a-bunch</p>
    <svg class="swoosh" viewBox="0 0 698 398" aria-hidden="true">
      <defs>
        <linearGradient id="sheen-front" x1="0" y1="0" x2="1" y2="0">
          <stop offset="0" stop-color="#1a1a18"/>
          <stop offset="0.45" stop-color="#9c9a90"/>
          <stop offset="0.8" stop-color="#f3f1e8"/>
          <stop offset="1" stop-color="#d9d5c3"/>
        </linearGradient>
      </defs>
      <path d="M0 396 C 250 372, 500 345, 698 288 L698 345 C 520 372, 260 386, 0 398 Z" fill="url(#sheen-front)"/>
      <path d="M20 398 C 300 386, 520 373, 698 355 L698 373 C 500 386, 300 394, 60 398 Z" fill="var(--green)"/>
    </svg>
  </section>

  <section class="card card--back" aria-label="Card back">
    <div class="contact">
      <h1 class="contact__name">NAME</h1>
      <p class="contact__title">Tital</p>
      <p class="contact__address">address</p>
      <ul class="contact__list contact__list--phones">
        <li>
          <svg class="contact__icon" viewBox="0 0 12 12" aria-hidden="true"><path d="M2 1 L4.5 1 L5 3.5 L3.8 4.5 C4.5 6 6 7.5 7.5 8.2 L8.5 7 L11 7.5 L11 10 C11 10.6 10.6 11 10 11 C5 11 1 7 1 2 C1 1.4 1.4 1 2 1 Z"/></svg>
          000.000.0000
        </li>
        <li>
          <svg class="contact__icon" viewBox="0 0 12 12" aria-hidden="true"><path d="M3.5 0.5 H8.5 V11.5 H3.5 Z M4.5 1.8 V9 H7.5 V1.8 Z"/></svg>
          000.000.0000
        </li>
        <li>
          <svg class="contact__icon" viewBox="0 0 12 12" aria-hidden="true"><path d="M3 1 H9 V4 H11 V9 H9 V11 H3 V9 H1 V4 H3 Z M4 7 V10 H8 V7 Z"/></svg>
          000.000.0000
        </li>
      </ul>
      <ul class="contact__list contact__list--online">
        <li>
          <svg class="contact__icon" viewBox="0 0 12 12" aria-hidden="true"><path d="M1 2.5 H11 V9.5 H1 Z"/></svg>
          ladyrust-a-bunch@mailbox.net
        </li>
        <li>
          <svg class="contact__icon" viewBox="0 0 12 12" aria-hidden="true"><circle cx="6" cy="6" r="5"/></svg>
          www.ladyrust-a-bunch.com
        </li>
      </ul>
    </div>
    <div class="brand-mark" aria-hidden="true"></div>
    <p class="brand-name">Lady Rust-a-bunch</p>
    <svg class="swoosh" viewBox="0 0 698 398" aria-hidden="true">
      <defs>
        <linearGradient id="sheen-back" x1="0" y1="0" x2="1" y2="0">
          <stop offset="0" stop-color="#1a1a18"/>
          <stop offset="0.45" stop-color="#9c9a90"/>
          <stop offset="0.8" stop-color="#f3f1e8"/>
          <stop offset="1" stop-color="#d9d5c3"/>
        </linearGradient>
      </defs>
      <path d="M0 396 C 250 372, 500 345, 698 295 L698 345 C 520 372, 260 386, 0 398 Z" fill="url(#sheen-back)"/>
      <path d="M20 398 C 300 386, 520 373, 698 355 L698 373 C 500 386, 300 394, 60 398 Z" fill="var(--green)"/>
    </svg>
  </section>

</main>
</body>
</html>
```